Male Chastity Keyholding Service Image

NOTE: ADULT ORIENTED PROJECTI am looking for a design that better communicates the service we offer in a more stylish approach. I have attached the current image we are utilizing for this Keyholding Service. The service we offer is we will ship the customer a padlock immediately with their order, then, based on the length of time the customer selected (1-6 weeks), we will ship the keys to them at a later time.The purpose of this service is to give customers whom do not have a partner to play the male chastity game with them an opportunity to experience real chastity without access to their keys.

Target Market(s)

Adult

Requirements
Nice to have
• Color Code - #8410ea
• This color is is our signature purple

```html
<!DOCTYPE html>
<html lang="en">
<head>
<meta charset="UTF-8">
<title>Male Chastity Keyholding Service</title>
<link rel="stylesheet" href="https://fonts.googleapis.com/css2?family=Montserrat:wght@400;500;800;900&family=Roboto:wght@400&display=swap">
<style>
  :root {
    --stage: #0a0b0d;
    --purple: #6b5596;
    --paper: #fafafa;
    --band: #e9e9e9;
    --ink: #3b3e3e;
    --text: #222222;
    --white: #ffffff;
  }
  * { margin: 0; padding: 0; box-sizing: border-box; }
  html, body { width: 1200px; height: 921px; overflow: hidden; background: var(--stage); }
  .stage { position: relative; width: 1200px; height: 921px; }
  .card {
    position: absolute; left: 402px; top: 181px; width: 396px; height: 558px;
    background: var(--paper); overflow: hidden;
  }
  .header {
    position: absolute; left: 0; top: 0; width: 100%; height: 87px;
    background: var(--purple); color: var(--white); text-align: center;
    font-family: "Montserrat", sans-serif;
  }
  .header-title { position: absolute; top: 14px; width: 100%; font-size: 29px; font-weight: 500; letter-spacing: 0.5px; line-height: 1; }
  .header-sub { position: absolute; top: 45px; width: 100%; font-size: 21px; font-weight: 500; letter-spacing: 2.2px; line-height: 1; }
  .headline { position: absolute; width: 100%; text-align: center; font-family: "Montserrat", sans-serif; line-height: 1; }
  .headline-main { top: 134px; font-size: 50px; font-weight: 900; color: var(--purple); letter-spacing: 0.5px; }
  .headline-sub { top: 185px; font-size: 25px; font-weight: 800; color: var(--ink); letter-spacing: 0.5px; }
  .timeline-band { position: absolute; left: 0; top: 247px; width: 100%; height: 163px; background: var(--band); }
  .later-panel {
    position: absolute; left: 170px; top: 234px; width: 260px; height: 189px;
    background: var(--purple); border-radius: 95px 0 0 95px;
  }
  .stage-label { position: absolute; font-family: "Montserrat", sans-serif; font-weight: 900; font-size: 24px; line-height: 1; text-align: center; width: 120px; }
  .stage-label.now { left: 25px; top: 263px; color: var(--purple); }
  .stage-label.later { left: 230px; top: 254px; color: var(--white); }
  .icon { position: absolute; }
  .icon-padlock { left: 40px; top: 292px; width: 92px; height: 104px; }
  .icon-keys { left: 268px; top: 288px; width: 72px; height: 116px; }
  .description {
    position: absolute; top: 455px; width: 100%; text-align: center;
    font-family: "Roboto", sans-serif; font-size: 13px; line-height: 16px; color: var(--text);
  }
  .keys-pill {
    position: absolute; left: 136px; top: 494px; width: 122px; height: 32px;
    border: 2px solid var(--purple); border-radius: 16px;
    font-family: "Montserrat", sans-serif; font-weight: 400; font-size: 19px; letter-spacing: 1px;
    color: var(--purple); text-align: center; line-height: 28px;
  }
  .footer-wedge { position: absolute; left: 0; bottom: 0; width: 396px; height: 22px; }
</style>
</head>
<body>
<div class="stage">
  <div class="card">
    <div class="header">
      <div class="header-title">MALE CHASTITY</div>
      <div class="header-sub">Keyholding Service</div>
    </div>

    <div class="headline headline-main">PADLOCK</div>
    <div class="headline headline-sub">IMMEDIATELY</div>

    <div class="timeline-band"></div>
    <div class="later-panel"></div>

    <div class="stage-label now">NOW</div>
    <div class="stage-label later">LATER</div>

    <svg class="icon icon-padlock" viewBox="0 0 92 104" aria-hidden="true">
      <path d="M8 48 V22 a16 16 0 0 1 32 0 V50" fill="none" stroke="#6b5596" stroke-width="5" stroke-linecap="round"/>
      <rect x="24" y="50" width="60" height="50" rx="3" fill="none" stroke="#6b5596" stroke-width="5"/>
      <circle cx="54" cy="70" r="5" fill="#6b5596"/>
      <path d="M51 72 L49 84 H59 L57 72 Z" fill="#6b5596"/>
    </svg>

    <svg class="icon icon-keys" viewBox="0 0 72 116" aria-hidden="true">
      <ellipse cx="22" cy="18" rx="12" ry="14" fill="none" stroke="#ffffff" stroke-width="4"/>
      <g fill="#ffffff">
        <path d="M30 36 l14 -4 l10 30 l18 34 l-5 4 l-6 -6 l-3 4 l-4 -5 l-16 -28 z"/>
        <path d="M8 34 h26 v34 h-7 v44 l-4 4 l-3 -5 v-8 h3 v-4 h-3 v-8 h3 v-4 h-3 v-19 h-7 z"/>
      </g>
      <g stroke="#6b5596" stroke-width="2">
        <line x1="11" y1="42" x2="31" y2="42"/>
        <line x1="11" y1="48" x2="31" y2="48"/>
        <line x1="11" y1="54" x2="31" y2="54"/>
        <line x1="11" y1="60" x2="31" y2="60"/>
        <line x1="36" y1="40" x2="44" y2="37"/>
        <line x1="38" y1="46" x2="46" y2="43"/>
      </g>
    </svg>

    <p class="description">Opportunity to experience real chastity<br>without access to their</p>
    <div class="keys-pill">KEYS</div>

    <svg class="footer-wedge" viewBox="0 0 396 22" preserveAspectRatio="none" aria-hidden="true">
      <polygon points="0,22 396,1 396,22" fill="#6b5596"/>
    </svg>
  </div>
</div>
</body>
</html>
```